Brightmoss Studies Flashcards Packaging and Logo!

Hi,
Hope you are well. I am looking for ideas for designs and logos for a box of flashcards to be released under the name “Brightmoss Studies”.
Box type: Top Bottom box
Box size: 6 x 2.7 x 3.3 inches
Box contents: multiplication flash cards with the question on one side and the answer on the other, to be used by children to learn the multiplication table
Design: I am looking for a simple design that is attractive to parents and children and highlights flashcards as simple, fun and easy to use.
Heading: large and clear “Multiplication Flash Cards”
Logo: should be small and in a corner along with the words “brightmoss studies”. Graphic should have some linkage to brightmoss studies. Maybe something related to learning or a rocket launch
Potential ideas to include on the cover or sides of the box:
- show a large picture of a flashcard on a ring
- show kid or two, having fun or happy
- use other educational graphics in the background or for the title e.g. notebook paper, book, teacher, launchpad, rocket launching, scroll, math graphics
Please leave room for 4 bullets to help describe the product
1. hole punched for organization
2. color coded for sorting
3. large clear numbers
4. self learning
Please let me know if you have any questions. I am attaching some pictures of other boxes so you have an idea but please note the designs should not be too similar or appear to be copies.
Thank you

Target Market(s)

targeting parents of children ages 6 years and above to buy flashcards online

Industry/Entity Type

Education

Logo Text

Brightmoss studies

Font styles to use
Serif
Sans Serif

Colors

Designer to choose colors to be used in the design.

Requirements
Must have
• for box:
• Title saying multiplication flash cards
• picture of flash card on ring
• clear and large font on the front
Nice to have
• pictures of kids
• some educational materials
Should not have
• blackboard
• too many different colors
• too much detail, especially on one side

```html
<!DOCTYPE html>
<html lang="en">
<head>
<meta charset="utf-8">
<title>Brightmoss Studies – Multiplication Flash Cards Packaging</title>
<link href="https://fonts.googleapis.com/css2?family=Open+Sans:wght@400;600;700;800&family=Cabin+Sketch:wght@700&family=Patrick+Hand&display=swap" rel="stylesheet">
<style>
  :root {
    --board-light: #6f7b7d;
    --board-dark: #454f51;
    --panel: #ffffff;
    --ink: #1c1c1c;
    --label: #f4f4f4;
    --sky: #7fcdf2;
    --blue: #3d8fe0;
    --orange: #f28a1a;
    --green: #8fd14f;
    --cyan: #12f0f8;
    --cyan-soft: #c9f6fb;
    --cloud: #d7f1fb;
    --cloud-line: #6cc3e4;
    --grid-bg: #f3f7fb;
    --grid-line: #dde8f2;
    --kids-a: #f1c7a0;
    --kids-b: #e8a7a0;
    --kids-c: #9fd0ea;
    --card-a: #f5efe2;
    --card-b: #ddd0b8;
  }
  * { margin: 0; padding: 0; box-sizing: border-box; }
  html, body { width: 1084px; height: 1200px; overflow: hidden; }
  body {
    position: relative;
    background: radial-gradient(ellipse at 55% 55%, var(--board-light) 0%, var(--board-dark) 100%);
    font-family: "Open Sans", Arial, sans-serif;
    color: var(--ink);
  }
  .board-label {
    position: absolute;
    font-family: "Cabin Sketch", "Comic Sans MS", cursive;
    font-weight: 700;
    font-size: 54px;
    color: var(--label);
    letter-spacing: 1px;
  }
  .panel { position: absolute; background: var(--panel); overflow: hidden; }
  .brand {
    position: absolute;
    display: flex; flex-direction: column; align-items: center;
    text-align: center; font-weight: 700; color: var(--ink); line-height: 1.05;
  }
  .brand-square { background: var(--orange); margin-bottom: 5px; }
  .title-main { font-weight: 800; letter-spacing: -0.5px; line-height: 1; white-space: nowrap; }
  .title-sub { font-weight: 700; line-height: 1; white-space: nowrap; }
  .waves { position: absolute; }

  /* Top */
  .lid { left: 217px; top: 36px; width: 659px; height: 294px; }
  .lid .heading { position: absolute; left: 34px; top: 56px; display: flex; flex-direction: column; align-items: flex-end; }
  .lid .title-main { font-size: 45px; letter-spacing: -1px; }
  .lid .title-sub { font-size: 30px; margin-top: 2px; }
  .lid .brand { right: 24px; top: 24px; width: 90px; font-size: 9px; }
  .lid .brand-square { width: 52px; height: 52px; }
  .features {
    position: absolute; left: 38px; top: 179px;
    display: grid; grid-template-columns: 208px 180px; row-gap: 10px;
    list-style: none; font-size: 12px; font-weight: 600;
  }
  .features li { display: flex; align-items: center; gap: 6px; }
  .features svg { width: 16px; height: 16px; flex: none; }
  .lid .waves { left: 0; bottom: 0; width: 659px; height: 150px; }

  /* Long side */
  .side-long {
    left: 217px; top: 354px; width: 659px; height: 361px;
    background-color: var(--grid-bg);
    background-image:
      linear-gradient(var(--grid-line) 1px, transparent 1px),
      linear-gradient(90deg, var(--grid-line) 1px, transparent 1px);
    background-size: 18px 18px;
  }
  .side-long .orange-field { position: absolute; inset: 0; width: 659px; height: 361px; }
  .kids-art {
    position: absolute; left: 0; top: 58px; width: 374px; height: 200px;
    border-radius: 60px 60px 0 0;
    background: linear-gradient(90deg, var(--kids-a) 0%, var(--kids-b) 45%, var(--kids-c) 100%);
  }
  .card-art {
    position: absolute; left: 372px; top: 40px; width: 240px; height: 340px;
    border-radius: 22px;
    transform: rotate(-14deg);
    background: linear-gradient(160deg, var(--card-a), var(--card-b));
    box-shadow: -6px 6px 14px rgba(0,0,0,0.18);
  }
  .cloud { position: absolute; left: 40px; top: 168px; width: 330px; height: 193px; }
  .cloud svg { position: absolute; inset: 0; width: 330px; height: 193px; }
  .cloud-text { position: absolute; left: 0; right: 0; top: 78px; text-align: center; }
  .cloud .tagline {
    font-family: "Patrick Hand", cursive; font-size: 22px; letter-spacing: 1px;
    display: inline-block; padding: 0 14px 2px; border-bottom: 1px dashed var(--cloud-line);
  }
  .cloud .title-main { font-size: 29px; margin-top: 6px; letter-spacing: -0.8px; }
  .cloud .title-sub {
    font-size: 20px; margin: 3px auto 0; width: 250px; padding-bottom: 4px;
    border-bottom: 1px dashed var(--cloud-line);
  }

  /* Short side */
  .side-short { left: 217px; top: 750px; width: 312px; height: 380px; }
  .side-short .brand { left: 0; right: 0; top: 18px; font-size: 9px; }
  .side-short .brand-square { width: 44px; height: 44px; }
  .cyan-band { position: absolute; left: 0; top: 155px; width: 312px; height: 82px; background: var(--cyan-soft); }
  .symbol-tile {
    position: absolute; left: 68px; top: 105px; width: 176px; height: 176px;
    background: var(--cyan); border-radius: 6px;
    color: #fff; font-size: 150px; font-weight: 600; line-height: 176px; text-align: center;
  }
  .side-short .title-main { position: absolute; left: 0; right: 0; top: 290px; text-align: center; font-size: 20px; }
  .side-short .title-sub { position: absolute; left: 0; right: 0; top: 314px; text-align: center; font-size: 14px; }
  .side-short .waves { left: 0; bottom: 0; width: 312px; height: 70px; }

  /* Logo */
  .logo-card { left: 700px; top: 805px; width: 220px; height: 268px; }
  .logo-card .brand { left: 0; right: 0; top: 58px; font-size: 21px; font-weight: 700; }
  .logo-card .brand-square { width: 96px; height: 96px; margin-bottom: 20px; }
</style>
</head>
<body>
  <div class="board-label" style="left:52px;top:165px;">TOP</div>
  <div class="board-label" style="left:42px;top:500px;">SIDE</div>
  <div class="board-label" style="left:42px;top:900px;">SIDE</div>
  <div class="board-label" style="left:748px;top:1098px;">LOGO</div>

  <section class="panel lid">
    <div class="heading">
      <div class="title-main">MULTIPLICATION</div>
      <div class="title-sub">FLASH CARDS</div>
    </div>
    <div class="brand"><span class="brand-square"></span>BRIGHTMOSS<br>STUDIES</div>
    <ul class="features">
      <li><svg viewBox="0 0 16 16"><rect x="1" y="3" width="11" height="11" fill="none" stroke="#333" stroke-width="1.5"/><path d="M3 8l3 3 8-9" fill="none" stroke="#f28a1a" stroke-width="2.5"/></svg>Hole punched for organization</li>
      <li><svg viewBox="0 0 16 16"><rect x="1" y="3" width="11" height="11" fill="none" stroke="#333" stroke-width="1.5"/><path d="M3 8l3 3 8-9" fill="none" stroke="#f28a1a" stroke-width="2.5"/></svg>Large clear numbers</li>
      <li><svg viewBox="0 0 16 16"><rect x="1" y="3" width="11" height="11" fill="none" stroke="#333" stroke-width="1.5"/><path d="M3 8l3 3 8-9" fill="none" stroke="#f28a1a" stroke-width="2.5"/></svg>Color coded for sorting</li>
      <li><svg viewBox="0 0 16 16"><rect x="1" y="3" width="11" height="11" fill="none" stroke="#333" stroke-width="1.5"/><path d="M3 8l3 3 8-9" fill="none" stroke="#f28a1a" stroke-width="2.5"/></svg>Self Learning</li>
    </ul>
    <svg class="waves" viewBox="0 0 659 150" preserveAspectRatio="none">
      <path d="M330 150 C430 110 520 40 659 20 L659 150 Z" fill="var(--sky)"/>
      <path d="M0 120 C180 150 380 120 520 70 C580 50 620 45 659 42 L659 60 C560 70 460 120 300 140 C180 150 80 140 0 128 Z" fill="var(--orange)"/>
      <path d="M350 120 C460 90 560 55 659 48 L659 56 C560 64 470 100 360 126 Z" fill="var(--green)"/>
      <path d="M380 140 C480 110 570 78 659 70 L659 95 C560 100 480 130 400 150 Z" fill="var(--blue)"/>
      <path d="M420 150 C500 130 580 110 659 105 L659 150 Z" fill="var(--sky)"/>
    </svg>
  </section>

  <section class="panel side-long">
    <svg class="orange-field" viewBox="0 0 659 361" preserveAspectRatio="none">
      <path d="M430 361 C430 200 480 80 560 0 L659 0 L659 361 Z" fill="var(--orange)"/>
      <path d="M345 361 C355 190 420 70 500 0 L528 0 C450 75 385 195 375 361 Z" fill="var(--sky)"/>
      <path d="M385 361 C395 210 445 100 515 20 L528 28 C460 108 412 215 405 361 Z" fill="var(--green)"/>
    </svg>
    <div class="kids-art" role="img" aria-label="Illustration of four happy cartoon children with backpacks"></div>
    <div class="card-art" role="img" aria-label="Illustration of multiplication flash cards held on a metal ring"></div>
    <div class="cloud">
      <svg viewBox="0 0 330 193" aria-hidden="true">
        <g fill="var(--cloud)">
          <circle cx="40" cy="70" r="40"/>
          <circle cx="105" cy="52" r="44"/>
          <circle cx="175" cy="48" r="46"/>
          <circle cx="240" cy="55" r="42"/>
          <circle cx="295" cy="72" r="35"/>
          <rect x="0" y="70" width="330" height="123"/>
        </g>
      </svg>
      <div class="cloud-text">
        <div class="tagline">FUN &amp; EASY-TO-USE</div>
        <div class="title-main">MULTIPLICATION</div>
        <div class="title-sub">FLASH CARDS</div>
      </div>
    </div>
  </section>

  <section class="panel side-short">
    <div class="brand"><span class="brand-square"></span>BRIGHTMOSS<br>STUDIES</div>
    <div class="cyan-band"></div>
    <div class="symbol-tile">X</div>
    <div class="title-main">MULTIPLICATION</div>
    <div class="title-sub">FLASH CARDS</div>
    <svg class="waves" viewBox="0 0 312 70" preserveAspectRatio="none">
      <path d="M0 62 C100 70 200 40 312 10 L312 22 C200 50 100 72 0 70 Z" fill="var(--orange)"/>
      <path d="M120 60 C200 40 260 25 312 22 L312 30 C250 34 190 50 130 66 Z" fill="var(--green)"/>
      <path d="M150 70 C220 50 270 38 312 34 L312 70 Z" fill="var(--sky)"/>
      <path d="M180 70 C240 55 280 48 312 46 L312 58 C280 60 240 66 210 70 Z" fill="var(--blue)"/>
    </svg>
  </section>

  <section class="panel logo-card">
    <div class="brand"><span class="brand-square"></span>BRIGHTMOSS<br>STUDIES</div>
  </section>
</body>
</html>
```